Core Values Poster for Healthcare company

Trying to Create a core values poster for my company. Healthcare Company - We have Neurosurgery, Pain Management, Physical Therapy, Occupational Therapy, Rehab, Imaging, and psychology so far and we are growing fast.

Core Values would Include - (Execution), (Loyalty), (Innovation), (Synergy), (Growth-Oriented), (Ethics & Integrity), (Love), and (Energy)

Please incorporate the Company Logo which is on the website and I have included it in my uploads. As long as the logo stays blue it does not need a gradient effect.

I like the posters made for this contest : https://pinlarkstudio.com.au/flyer-work/briefs/build-team-ideals-flyer-580316

This picture should be memorable so people know our Core Values

Target Market(s)

Staff in the company

Colors

Designer to choose colors to be used in the design.

Requirements
Must have
• Logo
Nice to have
• Pictures for each core value

```html
<!DOCTYPE html>
<html lang="en">
<head>
<meta charset="utf-8">
<title>Clearview Core Values</title>
<link rel="stylesheet" href="https://fonts.googleapis.com/css2?family=Cinzel:wght@400;500&family=Montserrat:wght@500&display=swap">
<style>
  :root {
    --brand-blue: #1f86c0;
    --band-blue: #2c4fbf;
    --sky-light: #d3eefb;
    --sky-mid: #a9dcf4;
    --sky-edge: #8ccdee;
    --card-white: #ffffff;
    --label-grey: #5a5a5a;
    --mark-grey: #a8a8a8;
    --execution: #a3155f;
    --loyalty: #f5b553;
    --innovation: #0e9b7e;
    --synergy: #1e9be0;
    --love: #d8252f;
    --energy: #3f9a1b;
    --growth: #27419a;
    --ethics: #6a11a0;
  }
  html, body { margin: 0; padding: 0; overflow: hidden; }
  body { width: 726px; height: 1200px; position: relative; background: radial-gradient(ellipse at 50% 45%, var(--sky-light) 0%, var(--sky-mid) 60%, var(--sky-edge) 100%); font-family: "Montserrat", sans-serif; }
  .poster-header { position: absolute; top: 0; left: 0; width: 726px; height: 128px; background: var(--card-white); display: flex; align-items: center; justify-content: center; gap: 16px; }
  .brand-square { width: 50px; height: 50px; border: 5px solid var(--brand-blue); box-sizing: border-box; }
  .brand-name { font-family: "Cinzel", serif; font-weight: 400; font-size: 58px; letter-spacing: 2px; color: var(--brand-blue); line-height: 1; }
  .title-band { position: absolute; top: 128px; left: 0; width: 726px; height: 56px; background: var(--band-blue); display: flex; align-items: center; justify-content: center; }
  .title-band h1 { margin: 0; font-family: "Cinzel", serif; font-weight: 400; font-size: 26px; letter-spacing: 9px; color: #fff; }
  .values-wheel { position: absolute; top: 0; left: 0; }
  .value-label { font-family: "Montserrat", sans-serif; font-weight: 500; font-size: 14px; fill: var(--label-grey); text-anchor: middle; dominant-baseline: middle; }
</style>
</head>
<body>
  <header class="poster-header">
    <div class="brand-square"></div>
    <div class="brand-name">CLEARVIEW</div>
  </header>
  <div class="title-band"><h1>CORE VALUES</h1></div>

  <svg class="values-wheel" width="726" height="1200" viewBox="0 0 726 1200" aria-label="Wheel of eight core values">
    <defs>
      <filter id="soft-shadow" x="-30%" y="-30%" width="160%" height="160%">
        <feDropShadow dx="0" dy="3" stdDeviation="5" flood-color="#3b7aa0" flood-opacity="0.28"/>
      </filter>
      <path id="value-card" d="M -51.3 -141 L -95.8 -263.1 A 280 280 0 0 1 95.8 -263.1 L 51.3 -141 A 150 150 0 0 0 -51.3 -141 Z" stroke="#fff" stroke-width="14" stroke-linejoin="round" fill="#fff"/>
      <path id="value-band" d="M -47 -144.6 L -55 -169.3 A 178 178 0 0 1 55 -169.3 L 47 -144.6 A 152 152 0 0 0 -47 -144.6 Z"/>
    </defs>

    <g transform="translate(363 690)">
      <g filter="url(#soft-shadow)">
        <use href="#value-card" transform="rotate(-22.5)"/>
        <use href="#value-card" transform="rotate(22.5)"/>
        <use href="#value-card" transform="rotate(67.5)"/>
        <use href="#value-card" transform="rotate(112.5)"/>
        <use href="#value-card" transform="rotate(157.5)"/>
        <use href="#value-card" transform="rotate(202.5)"/>
        <use href="#value-card" transform="rotate(247.5)"/>
        <use href="#value-card" transform="rotate(292.5)"/>
      </g>
      <use href="#value-band" transform="rotate(-22.5)" fill="var(--execution)"/>
      <use href="#value-band" transform="rotate(22.5)" fill="var(--loyalty)"/>
      <use href="#value-band" transform="rotate(67.5)" fill="var(--innovation)"/>
      <use href="#value-band" transform="rotate(112.5)" fill="var(--synergy)"/>
      <use href="#value-band" transform="rotate(157.5)" fill="var(--love)"/>
      <use href="#value-band" transform="rotate(202.5)" fill="var(--energy)"/>
      <use href="#value-band" transform="rotate(247.5)" fill="var(--growth)"/>
      <use href="#value-band" transform="rotate(292.5)" fill="var(--ethics)"/>

      <circle r="134" fill="#e9f6fc" opacity="0.7"/>
      <circle class="centre-disc" r="124" fill="#fff" filter="url(#soft-shadow)"/>
      <rect x="-46" y="-46" width="92" height="92" rx="10" fill="none" stroke="var(--mark-grey)" stroke-width="9"/>
    </g>

    <text class="value-label" transform="translate(281 491) rotate(-22.5)">EXECUTION</text>
    <text class="value-label" transform="translate(445 491) rotate(22.5)">LOYALTY</text>
    <text class="value-label" transform="translate(562 608) rotate(67.5)">INNOVATION</text>
    <text class="value-label" transform="translate(562 772) rotate(-67.5)">SYNERGY</text>
    <text class="value-label" transform="translate(445 889) rotate(-22.5)">LOVE</text>
    <text class="value-label" transform="translate(281 889) rotate(22.5)">ENERGY</text>
    <text class="value-label" transform="translate(164 772) rotate(-95)">GROWTH-ORIENTED</text>
    <text class="value-label" transform="translate(164 608) rotate(-67.5)">ETHICS &amp; INTEGRITY</text>

    <g class="value-icons" filter="url(#soft-shadow)" fill="#fff">
      <circle cx="229" cy="438" r="22"/>
      <circle cx="470" cy="426" r="22"/>
      <circle cx="638" cy="616" r="22"/>
      <circle cx="605" cy="841" r="22"/>
      <circle cx="403" cy="972" r="22"/>
      <circle cx="234" cy="944" r="22"/>
      <circle cx="88" cy="764" r="22"/>
      <circle cx="109" cy="561" r="22"/>
    </g>

    <!-- execution: person -->
    <g transform="translate(229 438)" fill="var(--execution)">
      <circle cx="-2" cy="-5" r="5"/>
      <path d="M -11 10 Q -10 1 -2 1 Q 6 1 7 10 Z"/>
      <circle cx="7" cy="6" r="3.5" fill="#d889b2"/>
    </g>
    <!-- loyalty: heart in hand -->
    <g transform="translate(470 426)" fill="var(--loyalty)">
      <path d="M 0 2 L -6 -4 A 3.4 3.4 0 0 1 0 -9 A 3.4 3.4 0 0 1 6 -4 Z"/>
      <path d="M -11 4 L -4 4 L 2 6 L 9 3 L 10 6 L 2 11 L -11 10 Z"/>
    </g>
    <!-- innovation: gear -->
    <g transform="translate(638 616)" fill="none" stroke="var(--innovation)" stroke-width="3">
      <circle r="6"/>
      <path d="M 0 -11 V -7 M 0 7 V 11 M -11 0 H -7 M 7 0 H 11 M -8 -8 L -5 -5 M 5 5 L 8 8 M 8 -8 L 5 -5 M -5 5 L -8 8"/>
    </g>
    <!-- synergy: orbit -->
    <g transform="translate(605 841)" fill="none" stroke="var(--synergy)" stroke-width="2">
      <ellipse rx="10" ry="4"/>
      <ellipse rx="10" ry="4" transform="rotate(60)"/>
      <ellipse rx="10" ry="4" transform="rotate(-60)"/>
      <circle r="2" fill="var(--synergy)"/>
    </g>
    <!-- love: heart -->
    <path transform="translate(403 972)" fill="var(--love)" d="M 0 8 L -8 0 A 4.6 4.6 0 0 1 0 -6 A 4.6 4.6 0 0 1 8 0 Z"/>
    <!-- energy: bolt in cycle -->
    <g transform="translate(234 944)">
      <circle r="10" fill="none" stroke="var(--energy)" stroke-width="2" stroke-dasharray="22 9"/>
      <path d="M 2 -7 L -4 1 L 0 1 L -2 7 L 4 -1 L 0 -1 Z" fill="var(--energy)"/>
    </g>
    <!-- growth: rising bars -->
    <g transform="translate(88 764)" fill="var(--growth)">
      <rect x="-10" y="2" width="4" height="7"/>
      <rect x="-4" y="-1" width="4" height="10"/>
      <rect x="2" y="-4" width="4" height="13"/>
      <path d="M -10 -2 L 4 -9" stroke="var(--growth)" stroke-width="2"/>
      <path d="M 10 -11 L 3 -11 L 8 -5 Z"/>
    </g>
    <!-- ethics: scales -->
    <g transform="translate(109 561)" stroke="var(--ethics)" stroke-width="2" fill="none">
      <path d="M 0 -10 V 9 M -6 9 H 6 M -10 -6 H 10"/>
      <path d="M -13 2 L -10 -6 L -7 2 Z M 7 2 L 10 -6 L 13 2 Z" fill="var(--ethics)"/>
    </g>
  </svg>
</body>
</html>
```